Corvell Health Booklet 2016

Corvell Health is a multi-specialty Practice in Midtown Manhattan offering advanced care in multiple areas of medicine. See our table of contents (PDF Uploaded)
Our designed booklet should be clean, easy to read, contemporary, high-end and elegant.
We need a general theme, Layout for cover and templates for internal.
We are entertaining the idea of two different sizes
8 x 10
or
11 x 8.5
Our tagline " The Future of Medicine is Here"
We will provide all the text content
The link to our website
www.CorvellHX.com
Uploaded files are as follows.. Logo, Our Team Photo and the PDF listing the table of contents.

```html
<!DOCTYPE html>
<html lang="en">
<head>
<meta charset="utf-8">
<title>Corvell Health Booklet – Pages 7 &amp; 8</title>
<link rel="stylesheet" href="https://fonts.googleapis.com/css2?family=Mulish:wght@300;400&family=Roboto:wght@300;400;700&display=swap">
<style>
  :root {
    --navy: #0b0f5c;
    --navy-text: #14195e;
    --orange: #e8940f;
    --body: #3c3c44;
    --paper: #ffffff;
    --canvas: #ffffff;
    --skin-pale: #f7ece4;
    --skin-light: #f0dccd;
    --skin-mid: #e6c6ae;
  }
  * { margin: 0; padding: 0; box-sizing: border-box; }
  html, body { width: 1200px; height: 1000px; overflow: hidden; background: var(--canvas); }
  .canvas { position: relative; width: 1200px; height: 1000px; }

  .spread {
    position: absolute; left: 15px; top: 270px; width: 1170px; height: 460px;
    background: var(--paper); overflow: hidden;
    box-shadow: 0 1px 5px rgba(0,0,0,.35);
  }
  .page { position: absolute; top: 0; width: 585px; height: 460px; }
  .page--left { left: 0; }
  .page--right { left: 585px; }

  .tab { position: absolute; top: 174px; width: 94px; height: 108px; background: var(--navy); border-radius: 50%; }
  .page--left .tab { left: -47px; }
  .page--right .tab { right: -47px; }

  .photo { position: absolute; top: 0; height: 460px; }
  .photo--skin-peel {
    left: 285px; width: 300px;
    background: linear-gradient(90deg, #ffffff 0%, var(--skin-pale) 18%, var(--skin-light) 100%);
  }
  .photo--injection {
    left: 0; width: 290px;
    background: linear-gradient(90deg, var(--skin-mid) 0%, var(--skin-light) 78%, #ffffff 100%);
  }

  .folio { position: absolute; top: 15px; font: 700 20px/1 'Roboto', sans-serif; }
  .folio--left { right: 18px; color: var(--navy); }
  .folio--right { left: 16px; color: var(--orange); }

  .column { position: absolute; color: var(--body); }
  .page--left .column { left: 55px; top: 36px; width: 207px; }
  .page--right .column { left: 317px; top: 24px; width: 201px; }

  .page-title {
    font: 300 19px/25px 'Mulish', sans-serif; color: var(--navy-text); margin-bottom: 8px;
  }
  .page--right .page-title { margin-bottom: 4px; }
  .section-title {
    font: 300 14px/16px 'Mulish', sans-serif; color: var(--navy-text); margin: 22px 0 8px;
  }
  .page--right .section-title { margin: 8px 0 0; }
  .page--right .section-title--treats { margin-top: 22px; }
  .body-copy {
    font: 400 6.7px/10.2px 'Roboto', sans-serif; text-align: justify; margin-bottom: 10px;
  }
  .page--right .body-copy--gap { margin-bottom: 11px; }

  .treat-list { list-style: none; margin-top: 1px; }
  .treat-list li {
    position: relative; padding-left: 7px;
    font: 400 6.7px/11.3px 'Roboto', sans-serif; color: var(--body);
  }
  .treat-list li::before {
    content: ""; position: absolute; left: 0; top: 2px; width: 3px; height: 7px;
    background: var(--orange); border-radius: 0 3px 3px 0;
  }

  .tagline {
    position: absolute; font: 700 11.5px/1 'Roboto', sans-serif;
    color: var(--navy-text); letter-spacing: .1px;
  }
  .page--left .tagline { left: 53px; top: 412px; }
  .page--right .tagline { left: 317px; top: 409px; }
</style>
</head>
<body>
<div class="canvas">
  <div class="spread">

    <section class="page page--left">
      <div class="tab"></div>
      <div class="photo photo--skin-peel" role="img" aria-label="Photo area: cosmetic skin rejuvenation portrait"></div>
      <span class="folio folio--left">7</span>

      <div class="column">
        <h1 class="page-title">Platelet (PRP) Injection<br>Cosmetic Rejuvenation</h1>
        <p class="body-copy">One of the newest uses of PRP is in the area of cosmetics. This includes PRP for wrinkle reduction, skin rejuvenation and scar reduction. This is now one of the fastest growing uses of PRP because of its natural origins and rapid ability to improve skin tone and texture. All without fillers or dangerous chemicals.</p>
        <p class="body-copy">Laboratory studies have shown that the increased concentration of growth factors in PRP can potentially speed up the healing and rejuvenating process, helping you to look your best and maintain your healthy glow.</p>
        <h2 class="section-title">Methodology:</h2>
        <p class="body-copy">After a consultation with our physicians, a sample of your blood is taken to extract the platets and concentrate them, where small injections are made in the areas to be treated. The concentrations of healing and growth factors in the injections can be 5-10 times those found in normal blood, accelerating the healing and rejuvenating process.</p>
        <p class="body-copy">Discover for yourself how this cutting-edge, simple procedure can help you look your best.</p>
      </div>

      <p class="tagline">HEALTH IS THE GREATEST WEALTH</p>
    </section>

    <section class="page page--right">
      <div class="tab"></div>
      <div class="photo photo--injection" role="img" aria-label="Photo area: cosmetic injection treatment close-up"></div>
      <span class="folio folio--right">8</span>

      <div class="column">
        <h1 class="page-title">Veltox: Pain/Cosmetics</h1>
        <p class="body-copy">Veltox has a wide range of applications in helping to reduce chronic pain and also in relaxing the muscles and skin for a more youthful appearance.</p>
        <p class="body-copy">Veltox is a medication directly injected into surface and muscular areas to cause a relaxation of nerve and muscle excitement.</p>
        <h2 class="section-title">For pain:</h2>
        <p class="body-copy">Veltox helps to relax spastic muscles that can contribute to chronic pain. This procedure can be helpful for those with nerve damage or neurological conditions that can cause spasticity and chronic pain.</p>
        <h2 class="section-title">For cosmetic:</h2>
        <p class="body-copy body-copy--gap">Veltox has been used with millions to reduce wrinkles and improve the appearance of skin tone. This is especially helpful in key areas such as in the forehead, around the eyes,</p>
        <p class="body-copy">mouth lines and at times the neck area. Veltox treatment is applied in a simple office procedure. Effects of the treatment can be seen within a few short days and last a considerable amount of time.</p>
        <h2 class="section-title section-title--treats">Veltox Treats:</h2>
        <ul class="treat-list">
          <li>Chronic Pain</li>
          <li>Spasticity</li>
          <li>Nerve Pain</li>
          <li>Acute Injury</li>
          <li>Nerve Pain</li>
          <li>Cosmetic Effects of Aging</li>
          <li>Persistent Pain from Old Injuries</li>
        </ul>
      </div>

      <p class="tagline">HEALTH IS THE GREATEST WEALTH</p>
    </section>

  </div>
</div>
</body>
</html>
```